Construction Company informative web page

Torvell Builders is a new company that combine Project Manager and kitchen & bath design with Interior remodeling for houses or business (commercial and residential construction)
We want to show our reviews, portafolio and background experience
Updates

Reason: I would like to have the time to interact with the favorite designers to fine tune the website also I'd like to see more designs

Hello Everybody,

Thank you for your time, please make the corrections shown below:

Pages:

1. Home:

1.  Includes a welcome and a briefly background:

2. Right side vertically show a few reviews with the option read more to open it, just the Name and last name, city and review (no start ratings)

3. Facebook and youtube link

4. Left side below shows 4 slides show with pictures and titles:

1. Kitchen Design

2. Bath Design

3. General Remodeling

4. Commercial Projects

2. About Us:

Our Professionals:

Torvell Builders Project Manager  is responsible to set the project schedule, request materials  and coordinate the delivery on time.  The Project Manager focus is ensuring  the best customer satisfaction in every step of the project until the final product is completed.

The Designer gives you the best ideas in 3D format,   getting the best lay out possible.  understanding your needs, defining your unique style putting together all your requirements and ideas to make the best match for you, making sure you get the best products within your budget

Torvell Builders have a high quality group of trade specialist; plumbers, electricians and installers. Our crew is pleasant to work with,  safety and cleaning values  and very detailed oriented

Our Core Values

As our slogan your project is our business, well we really mean it our job is not just to do the job is to guaranteed a pleasant experience with great costumer service, communication, quality, in time and within your budget

 

1. Services:

1. Commercial

2. Residential

2. Portafolio:  Separated pictures in each project, I want to have a brief description in each picture

1. Kitchen Design

2. Bath Design

3. General Remodeling

4. Commercial Projects

 

1. Contact Us:  

1. Project Management Department:

Contact Person: Rhonda Kestling

Email: rhonda@torvellbuilders.com

2. Office Management Department:

Contact Person: Lou Brambery

Email: info@torvellbuilders.com

 

Please try to pick design style shown in business card to match a little bit. Keep the color tones

I want the logo in the upper left corner and a very nice picture with a kitchen (warm colors)mostly American northeast style like the main pic of the web.

I want the web page is able to be fully open in computers, tablets and cellphones

Please send me an email to torvellbuilders1@mailnest.com so I can send you my logo and any other information to be incorporated

Thank you

Hello Everybody,

Thank you for your time, please make the corrections accordingly:

Pages:

1. Home: Includes a welcome and a briefly say something about our background 

Hello, I just upload my logo and my business card so you can adjust your designs

Please presented responsive format

I want coding the webpage too

Please read carefully my last update

Thank you so much!                                   

Industry/Entity Type

Residential

Requirements
Nice to have
• Should it has a Newsletter subscription with the email at the bottom of the home page
In contact page: A box "Contact us for a free estimate"

```html
<!DOCTYPE html>
<html lang="en">
<head>
<meta charset="utf-8">
<title>Torvell Builders</title>
<link href="https://fonts.googleapis.com/css2?family=Arimo:wght@400;700&family=Tinos:ital@1&display=swap" rel="stylesheet">
<style>
:root{
  --bg:#e9e9e9;
  --maroon:#7a2422;
  --accent:#c8382c;
  --heading:#7d2a27;
  --text:#4a4a4a;
  --muted:#777;
  --rule:#d8d8d8;
  --footer:#3a3a3a;
  --footer-text:#cfcfcf;
}
*{box-sizing:border-box;margin:0;padding:0}
html,body{width:902px;height:1200px;overflow:hidden;background:var(--bg);font-family:"Arimo",Arial,sans-serif;color:var(--text);-webkit-font-smoothing:antialiased;-moz-osx-font-smoothing:grayscale}
.mono-text{filter:grayscale(1)}
.flat-text{will-change:transform}
.page{position:absolute;left:130px;top:0;width:645px;height:1200px;background:#fff}
.site-header{position:absolute;left:0;top:0;width:645px;height:66px;background:var(--maroon)}
.brand{position:absolute;left:12px;top:22px;display:flex;align-items:center;gap:6px;color:#f3e6d6;font-size:13px;font-weight:700}
.brand-mark{width:14px;height:14px;background:#f3e6d6}
.main-nav{position:absolute;top:29px;left:0;font-size:8px;color:#fff}
.main-nav a{position:absolute;white-space:nowrap;color:#fff;text-decoration:none}
.hero{position:absolute;left:0;top:66px;width:645px;height:346px;background:linear-gradient(160deg,#6b4a3a 0%,#4a3025 35%,#a9a29c 60%,#7e7874 100%)}
.hero-caption{position:absolute;left:0;bottom:0;width:645px;height:70px;background:rgba(30,30,30,.82);color:#fff}
.hero-caption h2{position:absolute;left:24px;top:10px;font-family:"Tinos",serif;font-style:italic;font-weight:400;font-size:18px}
.hero-caption p{position:absolute;left:23px;top:37px;font-size:8.8px;white-space:nowrap}
.arrows{position:absolute;display:flex;gap:1px}
.arrows span{display:block;background:var(--accent)}
.arrows svg{display:block}
.section-title{position:absolute;font-family:"Tinos",serif;font-style:italic;font-weight:400;color:var(--heading);font-size:19px}
.intro{position:absolute;left:26px;top:464px;width:594px;text-align:center;font-size:7.6px;line-height:16px;color:var(--text)}
.divider{position:absolute;left:12px;width:621px;height:1px;background:var(--rule)}
.review{position:absolute;top:591px;width:187px}
.review .photo{height:125px}
.review h3{margin:13px 1px 0;font-size:9px;font-weight:400;color:var(--heading)}
.review p{margin:4px 2px 0;font-size:7.4px;line-height:16px;color:var(--text)}
.review .meta{margin-top:7px;border-top:1px solid var(--rule);padding:7px 1px 0;font-size:8.6px;color:var(--heading)}
.review .meta em{color:var(--muted);font-size:7.2px}
.review .meta i{color:#aaa;font-style:normal;margin:0 4px}
.tile{position:absolute;width:115px;height:108px}
.tile .label{position:absolute;left:0;bottom:0;width:100%;height:19px;background:rgba(20,20,20,.85);color:#fff;font-size:8.2px;padding:4px 8px}
.site-footer{position:absolute;left:0;top:1131px;width:645px;height:69px;background:var(--footer);color:var(--footer-text)}
.foot-nav{position:absolute;left:18px;top:20px;font-size:7.2px;white-space:nowrap}
.foot-nav i{font-style:normal;margin:0 12px}
.copy{position:absolute;left:18px;top:40px;font-size:7.2px}
.social{position:absolute;left:557px;top:26px;display:flex;gap:4px}
.social span{width:15px;height:15px;border-radius:50%;background:#6d6f76}
</style>
</head>
<body>
<div class="page">
  <header class="site-header">
    <div class="brand flat-text"><span class="brand-mark"></span>Torvell Builders</div>
    <nav class="main-nav flat-text">
      <a style="left:155px">Home</a>
      <a style="left:216px">About Us</a>
      <a style="left:289px">Customer Reviews</a>
      <a style="left:394px">Our Portfolio</a>
      <a style="left:479px">Testimonials</a>
      <a style="left:563px">Contact us</a>
    </nav>
  </header>

  <section class="hero" role="img" aria-label="Modern kitchen with dark wood cabinets, white island and pendant lights">
    <div class="hero-caption">
      <h2 class="flat-text">Torvell Builders</h2>
      <p class="mono-text">uncover many web sites still in their infancy. Various versions have evolved over the years, sometimes by accident, sometimes on purpose</p>
      <div class="arrows" style="left:595px;top:28px">
        <span><svg width="20" height="20"><path d="M12 5 7 10l5 5" stroke="#fff" fill="none" stroke-width="1.3"/></svg></span>
        <span><svg width="20" height="20"><path d="M8 5l5 5-5 5" stroke="#fff" fill="none" stroke-width="1.3"/></svg></span>
      </div>
    </div>
  </section>

  <h2 class="section-title flat-text" style="left:0;width:645px;text-align:center;top:430px">Background Experience</h2>
  <p class="intro mono-text">It is a long established fact that a reader will be distracted by the readable content of a page when looking at its layout. The point of using Lorem Ipsum is that it has a more-or-less normal distribution of letters, as opposed to using 'Content here, content here', making it look like readable English. Many desktop publishing packages and web page editors now use Lorem Ipsum as their default model text...</p>
  <div class="divider" style="top:533px"></div>

  <h2 class="section-title flat-text" style="left:12px;top:548px">Customer Reviews</h2>
  <div class="arrows" style="left:603px;top:555px">
    <span><svg width="12" height="13"><path d="M7 3 4 6.5 7 10" stroke="#fff" fill="none"/></svg></span>
    <span><svg width="12" height="13"><path d="M5 3l3 3.5L5 10" stroke="#fff" fill="none"/></svg></span>
  </div>

  <article class="review" style="left:12px">
    <div class="photo" role="img" aria-label="Portrait of a smiling customer on the phone" style="background:linear-gradient(135deg,#f2ede8,#d9b9a0 55%,#f4f1ee)"></div>
    <h3 class="flat-text">It is a long established fact</h3>
    <p class="mono-text">It is a long established fact that a reader will be distracted by the readable content...</p>
    <div class="meta flat-text">Mason Keller<i>/</i><em>Posted on 27 Feb 2014</em></div>
  </article>
  <article class="review" style="left:229px;width:183px">
    <div class="photo" role="img" aria-label="Portrait of a smiling customer" style="background:linear-gradient(135deg,#efe6df,#9a5a3c 50%,#e8d8cc)"></div>
    <h3 class="flat-text">It is a long established fact</h3>
    <p class="mono-text">It is a long established fact that a reader will be distracted by the readable content...</p>
    <div class="meta flat-text">Mason Keller<i>/</i><em>Posted on 27 Feb 2014</em></div>
  </article>
  <article class="review" style="left:444px">
    <div class="photo" role="img" aria-label="Portrait of a smiling customer at a laptop" style="background:linear-gradient(135deg,#4f6b3a,#7a9bc2 55%,#d6dde6)"></div>
    <h3 class="flat-text">It is a long established fact</h3>
    <p class="mono-text">It is a long established fact that a reader will be distracted by the readable content...</p>
    <div class="meta flat-text">Mason Keller<i>/</i><em>Posted on 27 Feb 2014</em></div>
  </article>
  <div class="divider" style="top:832px"></div>

  <h2 class="section-title flat-text" style="left:12px;top:846px">Our Portfolio</h2>
  <div class="arrows" style="left:604px;top:856px">
    <span><svg width="12" height="13"><path d="M7 3 4 6.5 7 10" stroke="#fff" fill="none"/></svg></span>
    <span><svg width="12" height="13"><path d="M5 3l3 3.5L5 10" stroke="#fff" fill="none"/></svg></span>
  </div>

  <div class="tile" style="left:11px;top:886px;background:linear-gradient(160deg,#3b3b3b,#d9d4d0 60%,#6a2a2a)" role="img" aria-label="Modern kitchen project"><span class="label mono-text">Modern Kichen &raquo;</span></div>
  <div class="tile" style="left:137px;top:886px;background:linear-gradient(160deg,#e8e2da,#8a6a4e 60%,#f1ece6)" role="img" aria-label="Modern kitchen project"><span class="label mono-text">Modern Kichen &raquo;</span></div>
  <div class="tile" style="left:264px;top:886px;background:linear-gradient(160deg,#d9dde0,#8d8f92 55%,#e9e7e3)" role="img" aria-label="Bathroom project"><span class="label mono-text">Bothroom &raquo;</span></div>
  <div class="tile" style="left:390px;top:886px;background:linear-gradient(160deg,#6a4a33,#c29668 55%,#8c6a4d)" role="img" aria-label="Bathroom project"><span class="label mono-text">Bothroom &raquo;</span></div>
  <div class="tile" style="left:516px;top:886px;background:linear-gradient(160deg,#b69478,#ece7e2 55%,#9fb3c0)" role="img" aria-label="Bathroom project"><span class="label mono-text">Bothroom &raquo;</span></div>

  <div class="tile" style="left:11px;top:1006px;background:linear-gradient(160deg,#e0d1bf,#9a6e4a 55%,#efe8e0)" role="img" aria-label="Bathroom project"><span class="label mono-text">Bothroom &raquo;</span></div>
  <div class="tile" style="left:137px;top:1006px;background:linear-gradient(160deg,#efe6d4,#a87a52 60%,#d7c7b0)" role="img" aria-label="Bathroom project"><span class="label mono-text">Bothroom &raquo;</span></div>
  <div class="tile" style="left:264px;top:1006px;background:linear-gradient(160deg,#1e1e1e,#7e6c5e 55%,#2a2a2a)" role="img" aria-label="Modern kitchen project"><span class="label mono-text">Modern Kichen &raquo;</span></div>
  <div class="tile" style="left:390px;top:1006px;background:linear-gradient(160deg,#4a3a30,#d8d3cf 50%,#6b4b38)" role="img" aria-label="Modern kitchen project"><span class="label mono-text">Modern Kichen &raquo;</span></div>
  <div class="tile" style="left:516px;top:1006px;background:linear-gradient(160deg,#f1f1f1,#4a4544 55%,#cfcfcf)" role="img" aria-label="Modern kitchen project"><span class="label mono-text">Modern Kichen &raquo;</span></div>

  <footer class="site-footer">
    <div class="foot-nav mono-text">Home<i>|</i>About Us<i>|</i>Customer Reviews<i>|</i>Our Portfolio<i>|</i>Testimonials<i>|</i>Contact us</div>
    <div class="copy mono-text">&copy; 2014. Torvell Builders. All Rights Reserved.</div>
    <div class="social" aria-label="Social links"><span></span><span></span><span></span><span></span></div>
  </footer>
</div>
</body>
</html>
```